Korvane Development and Management Corp. Business Card

A logo design project has been started for our Calgary-Alberta, Canada based land development and project management company. Using this logo, a clean, sleek, professional business card is to be developed (for digital or print media) representing the principals of the company (community, sustainability, and harmony).
Updates

Reason: Logo design recently completed.

Adobe Illustrator Vector file uploaded. Thanks, Lev

Target Market(s)

Similar business development professionals and other engineering project management personnel involved in land developemtn. Also used to as as the brand and image with both private individuals (Landowners), public officials (policy makers), and investors (banks, venture capitalists).

Industry/Entity Type

Digital

Requirements
Must have
• Open to designers opinion. Based on logo. Must have logo, and space for employee name, title, address, website, office / cell numbers.
Should not have
• No Palm trees or tropical references. Company is based in Calgary, Alberta, Canada.

```html
<!DOCTYPE html>
<html lang="en">
<head>
<meta charset="utf-8">
<title>Korvane Development and Management Corp. — Business Card</title>
<link rel="stylesheet" href="https://fonts.googleapis.com/css2?family=Open+Sans:wght@400;600&display=swap">
<style>
  :root {
    --page: #e6e7e9;
    --card-dark: #2b2f37;
    --card-light: #ffffff;
    --lime: #9cc43a;
    --grey-text: #7d828a;
    --grey-soft: #5a5f67;
    --ink: #2b2f37;
    --white: #ffffff;
  }
  * { box-sizing: border-box; margin: 0; padding: 0; }
  html, body {
    width: 1200px; height: 676px; overflow: hidden;
    background: var(--page);
    font-family: "Open Sans", Arial, sans-serif;
  }
  .sheet {
    position: relative; width: 1200px; height: 676px;
    display: flex; align-items: center; justify-content: center; gap: 40px;
  }
  .card {
    position: relative; width: 540px; height: 309px; overflow: hidden;
    box-shadow: 0 6px 18px rgba(0,0,0,.18);
  }
  .corner-fill {
    position: absolute; right: 0; bottom: 0; width: 200px; height: 40px;
    background: linear-gradient(to right, rgba(156,196,58,0), var(--lime) 70%);
  }

  /* front */
  .card-front { background: var(--card-dark); }
  .card-front .accent-line {
    position: absolute; left: 0; right: 0; top: 262px; height: 3px; background: var(--lime);
  }
  .card-front .brand { position: absolute; left: 60px; top: 72px; }
  .brand-mark { display: flex; align-items: center; gap: 12px; }
  .brand-square { width: 34px; height: 34px; background: var(--lime); }
  .brand-name {
    font-size: 46px; font-weight: 400; letter-spacing: 2px; color: var(--lime); line-height: 1;
  }
  .card-front .tagline {
    margin-top: 8px; margin-left: 46px; font-size: 13px; color: var(--grey-text);
  }
  .card-front .website {
    position: absolute; left: 60px; top: 188px; font-size: 19px; letter-spacing: .5px; color: var(--grey-soft);
  }
  .card-front .website .domain { color: var(--lime); }

  /* back */
  .card-back { background: var(--card-light); }
  .card-back .band {
    position: absolute; left: 0; right: 0; bottom: 0; height: 96px; background: var(--card-dark);
    border-top: 3px solid var(--lime);
  }
  .card-back .brand { position: absolute; left: 40px; top: 92px; }
  .card-back .brand-square { width: 22px; height: 22px; }
  .card-back .brand-name { font-size: 28px; letter-spacing: 1.5px; }
  .card-back .tagline { margin-top: 4px; margin-left: 34px; font-size: 8.5px; color: var(--grey-text); }
  .divider {
    position: absolute; left: 272px; top: 68px; width: 1px; height: 118px; background: #b9bcc1;
  }
  .contact-list { position: absolute; left: 290px; top: 72px; list-style: none; }
  .contact-list li {
    display: flex; align-items: flex-start; gap: 9px; font-size: 12.5px; line-height: 1.25;
    color: var(--ink); margin-bottom: 4px;
  }
  .contact-list li.address { color: var(--lime); }
  .contact-list svg { flex: none; width: 11px; height: 11px; margin-top: 2px; fill: var(--lime); }
  .person { position: absolute; left: 200px; bottom: 38px; text-align: center; color: var(--white); }
  .person-name { font-size: 21px; font-weight: 400; line-height: 1.1; }
  .person-title { font-size: 12px; color: #d9dbde; }
</style>
</head>
<body>
<main class="sheet">
  <section class="card card-front" aria-label="Card front">
    <div class="brand">
      <div class="brand-mark"><span class="brand-square"></span><span class="brand-name">KORVANE</span></div>
      <p class="tagline">Development and Management Corp.</p>
    </div>
    <p class="website">www.<span class="domain">yourwebsite</span>.com</p>
    <div class="accent-line"></div>
    <div class="corner-fill" role="img" aria-label="Lime decorative corner accent"></div>
  </section>

  <section class="card card-back" aria-label="Card back">
    <div class="brand">
      <div class="brand-mark"><span class="brand-square"></span><span class="brand-name">KORVANE</span></div>
      <p class="tagline">Development and Management Corp.</p>
    </div>
    <div class="divider"></div>
    <ul class="contact-list">
      <li class="address">
        <svg viewBox="0 0 12 12"><path d="M6 0a4 4 0 0 0-4 4c0 3 4 8 4 8s4-5 4-8a4 4 0 0 0-4-4zm0 5.6A1.6 1.6 0 1 1 6 2.4a1.6 1.6 0 0 1 0 3.2z"/></svg>
        <span>address (street address<br>suite number, city, state, zip</span>
      </li>
      <li>
        <svg viewBox="0 0 12 12"><path d="M2 1h3l1 3-2 1a7 7 0 0 0 3 3l1-2 3 1v3a1 1 0 0 1-1 1A10 10 0 0 1 1 2a1 1 0 0 1 1-1z"/></svg>
        <span>0123 456 789</span>
      </li>
      <li>
        <svg viewBox="0 0 12 12"><path d="M3 0h6a1 1 0 0 1 1 1v10a1 1 0 0 1-1 1H3a1 1 0 0 1-1-1V1a1 1 0 0 1 1-1zm0 2v7h6V2z"/></svg>
        <span>0123 456 789</span>
      </li>
      <li>
        <svg viewBox="0 0 12 12"><path d="M0 2h12v8H0zm1 1v.5l5 3 5-3V3z"/></svg>
        <span>youremail@mail.com</span>
      </li>
      <li>
        <svg viewBox="0 0 12 12"><circle cx="6" cy="6" r="5.5"/></svg>
        <span>www.yourwebsite.com</span>
      </li>
    </ul>
    <div class="band"></div>
    <div class="person">
      <p class="person-name">your name</p>
      <p class="person-title">designation</p>
    </div>
    <div class="corner-fill" role="img" aria-label="Lime decorative corner accent"></div>
  </section>
</main>
</body>
</html>
```